We need a new e-commerce website. Designed and fully functional.

We are looking for someone who can re-create our website from A-Z and it is fully functional (turnkey). Currently we have a website that we do not like because it is too dark and not easy to use. We would like a more modern, minimalist, elegant, bright and very easy to use. We are also looking for a person who would agree to accompany us in the catalog (with payment in addition to race). To be defined later. We are a designer company, sold through the online store. The jewels are long necklaces with thematic pendants associated with semi-precious stones. 6 themes of pendants, 2 colors and 6 types of semi-precious stones that are combined according to desires. 72 possibilities of combinations. We already have all the connections, texts, payment possibilities, pictures that we all put at your disposal. You can have a look on our website on velmorik.com. We also have a little guide (attached) of what we are looking for this new website. The site must be in 2 languages (French-English) and 3 currencies (dollar, euro and Swiss francs). The shipping costs must be displayed according to the country of destination (KDX) in the shopping cart and for Switzerland the VAT must be displayed directly too. Name of the website: trévi manu jewelry (www.velmorik.com) E-Mail address for the website: info@velmorik.com This website must contain: Home: home page. Welcome page Shop: All articles About: About the creator Contact: e-mail and company contact Press: all the publications in the magazines FAQ & HELP: the company information, orders ... Account: the clients can create an account if they want Purchasing Pannier Languages: English-French Currencies: Dollar, Euro, Swiss Francs

Industry/Entity Type

Jewelry Store

Coding

Coded - Design and coding required

Font styles to use
Sans Serif

Colors

Designer to choose colors to be used in the design.

Requirements
Must have
• This website must be easy to use, modern, elegant and sober.

```html
<!DOCTYPE html>
<html lang="en">
<head>
<meta charset="utf-8">
<title>trévi manu jewelry — Home</title>
<link href="https://fonts.googleapis.com/css2?family=Montserrat:wght@400;500;600;700&family=Open+Sans:wght@400;600&display=swap" rel="stylesheet">
<style>
:root{
  --stage:#d9d9d9;
  --white:#ffffff;
  --ink:#2b2b2b;
  --muted:#8a8a8a;
  --line:#e3e3e3;
  --plum-dark:#2e1522;
  --plum:#6b3a50;
  --gold:#e3a332;
  --rose:#d09996;
  --footer:#2f2f2f;
  --footer-text:#bdbdbd;
}
*{box-sizing:border-box;margin:0;padding:0}
html,body{width:780px;height:1200px;overflow:hidden;background:var(--stage)}
body{font-family:"Open Sans",Arial,sans-serif;color:var(--ink)}
.page{position:absolute;left:215px;top:8px;width:700px;height:2368px;background:var(--white);transform:scale(.5);transform-origin:0 0;overflow:hidden;box-shadow:0 2px 8px rgba(0,0,0,.15)}
.topbar{height:18px;border-bottom:1px solid var(--line);display:flex;justify-content:space-between;align-items:center;padding:0 70px;font-size:7px;color:var(--muted)}
.topbar span{margin-left:10px}
.header{height:67px;display:flex;align-items:center;padding:0 72px;justify-content:space-between}
.brand{display:flex;flex-direction:column;align-items:center}
.brand-mark{width:12px;height:12px;border:1px solid var(--ink);border-radius:50%;margin-bottom:3px}
.brand-name{font-family:"Montserrat",sans-serif;font-size:15px;letter-spacing:1px;font-weight:500}
.brand-sub{font-family:"Montserrat",sans-serif;font-size:5px;letter-spacing:5px;font-weight:500}
.nav{display:flex;gap:12px;font-family:"Montserrat",sans-serif;font-size:8px;font-weight:600;margin-left:50px}
.nav-tools{margin-left:auto;display:flex;gap:10px;align-items:center}
.hero{height:265px;background:radial-gradient(ellipse at 25% 30%,#8a5a6c 0%,var(--plum) 30%,var(--plum-dark) 80%);position:relative;color:var(--white);text-align:center}
.hero-text{position:absolute;left:0;right:0;top:85px}
.hero h1{font-family:"Montserrat",sans-serif;font-size:24px;font-weight:500;letter-spacing:.5px}
.hero p{font-size:9px;margin:6px 0 10px}
.btn-outline{display:inline-block;border:1px solid currentColor;font-family:"Montserrat",sans-serif;font-size:8px;font-weight:600;padding:6px 14px;letter-spacing:.5px}
.hero-controls{position:absolute;left:0;right:0;bottom:18px;display:flex;justify-content:center;gap:14px}
.section-title{font-family:"Montserrat",sans-serif;font-size:13px;font-weight:700;text-align:center;letter-spacing:.3px}
.section-lead{font-size:7px;text-align:center;color:var(--muted);margin-top:6px}
.themes{padding-top:48px}
.theme-grid{width:423px;margin:22px auto 0;display:grid;grid-template-columns:repeat(3,127px);column-gap:21px;row-gap:40px}
.theme-photo{height:95px}
.theme{text-align:center}
.theme h3{font-family:"Montserrat",sans-serif;font-size:10px;font-weight:700;letter-spacing:1.5px;margin-top:9px}
.theme small{display:block;font-size:6px;color:var(--muted);margin:4px 0 8px;letter-spacing:.5px}
.btn-mini{display:inline-block;border:1px solid var(--ink);font-family:"Montserrat",sans-serif;font-size:5px;font-weight:600;padding:3px 9px}
.divider{width:560px;margin:42px auto 0;border-top:1px solid var(--line)}
.shop{padding-top:44px}
.product-grid{width:557px;margin:20px auto 0;display:grid;grid-template-columns:repeat(4,131px);column-gap:11px;row-gap:36px}
.product-card{border:1px solid var(--line);height:178px;position:relative}
.necklace{width:100%;height:100%}
.cart-bar{position:absolute;left:0;right:0;bottom:0;height:16px;background:var(--ink);color:var(--white);font-size:6px;font-family:"Montserrat",sans-serif;font-weight:600;display:flex;align-items:center;padding:0 6px;gap:14px}
.product-info{text-align:center;margin-top:8px}
.product-info h4{font-size:7px;font-weight:600}
.stars{font-size:7px;color:#cfcfcf;letter-spacing:1px;margin:3px 0}
.price{font-size:7px;font-weight:600}
.price s{color:var(--muted);font-weight:400;margin-left:3px}
.view-more{text-align:center;margin-top:26px}
.promo{margin-top:42px;height:182px;background:var(--rose);position:relative;color:var(--white);text-align:center}
.promo-portrait{position:absolute;left:70px;bottom:0;width:120px;height:182px;background:linear-gradient(180deg,#b58572 0%,#8e5e4c 55%,#2a2324 100%)}
.promo-text{position:absolute;left:140px;right:0;top:48px}
.promo h2{font-family:"Montserrat",sans-serif;font-size:13px;font-weight:700}
.promo p{font-size:7px;color:#f6e1e0;margin-top:7px;line-height:1.6}
.promo .btn-outline{font-size:6px;padding:5px 10px;margin-top:8px}
.blog{padding-top:50px}
.blog-grid{width:554px;margin:18px auto 0;display:grid;grid-template-columns:267px 267px;column-gap:20px}
.blog-photo{height:157px}
.blog-body{display:flex;gap:10px;margin-top:12px}
.date{width:18px;flex:none;text-align:center;font-size:6px;font-family:"Montserrat",sans-serif;font-weight:600}
.date b{display:block;background:var(--ink);color:var(--white);padding:3px 0}
.date i{display:block;font-style:normal;padding:3px 0;background:#555;color:var(--white)}
.blog-body h5{font-family:"Montserrat",sans-serif;font-size:6.5px;font-weight:700}
.blog-body p{font-size:5.5px;color:var(--muted);line-height:1.6;margin-top:5px}
.footer{position:absolute;left:0;right:0;bottom:0;height:294px;background:var(--footer);color:var(--footer-text);font-size:6px}
.partners{display:flex;justify-content:space-between;padding:36px 100px 0;color:var(--white);font-family:"Montserrat",sans-serif;font-size:9px;font-weight:700}
.foot-cols{display:grid;grid-template-columns:127px 207px 180px;padding:52px 0 0 99px}
.foot-cols h6,.foot-links h6{font-family:"Montserrat",sans-serif;font-size:7px;font-weight:600;color:var(--white);margin-bottom:6px}
.foot-cols p{line-height:1.7}
.socials{display:flex;gap:4px;margin-top:6px}
.socials span{width:9px;height:9px;border:1px solid var(--footer-text);border-radius:50%}
.subscribe{display:flex;margin-top:10px}
.subscribe span{width:108px;height:16px;background:var(--white);color:#999;padding:4px 6px;font-size:5.5px}
.subscribe b{height:16px;padding:4px 8px;color:var(--white);font-size:5.5px;font-family:"Montserrat",sans-serif}
.foot-links{display:grid;grid-template-columns:158px 83px 75px 80px 120px;padding:26px 0 0 99px}
.foot-links li{list-style:none;line-height:1.8;font-size:5.5px}
.foot-brand .brand-name,.foot-brand .brand-sub{color:var(--white)}
.foot-brand .brand-mark{border-color:var(--white)}
.foot-brand p{margin-top:6px;line-height:1.6;font-size:5.5px}
.insta{display:grid;grid-template-columns:repeat(4,28px);gap:2px}
.insta span{height:24px;background:linear-gradient(135deg,#d9c7b6,#9a7760)}
.copyright{position:absolute;left:0;right:0;bottom:14px;text-align:center;font-size:5.5px}
</style>
</head>
<body>
<div class="page">

  <div class="topbar"><div>USD ⌄</div><div><span>ENG ⌄</span><span>Gift Certificates</span><span>♥ Wishlist</span><span>Sign / Register</span></div></div>

  <header class="header">
    <div class="brand"><div class="brand-mark"></div><div class="brand-name">TRÉVI MANU</div><div class="brand-sub">JEWELRY</div></div>
    <nav class="nav"><span>HOME</span><span>ABOUT</span><span>SHOP</span><span>CONTACT</span><span>PRESS</span><span>FAQ &amp; HELP</span></nav>
    <div class="nav-tools">
      <svg width="9" height="9" viewBox="0 0 10 10"><circle cx="4" cy="4" r="3" fill="none" stroke="#2b2b2b" stroke-width="1.2"/><line x1="6.2" y1="6.2" x2="9" y2="9" stroke="#2b2b2b" stroke-width="1.2"/></svg>
      <svg width="12" height="11" viewBox="0 0 12 11"><path d="M1 2h2l1.5 5h5L11 3H4" fill="none" stroke="#2b2b2b" stroke-width="1"/><circle cx="5" cy="9.5" r="1" fill="#2b2b2b"/><circle cx="9" cy="9.5" r="1" fill="#2b2b2b"/><circle cx="10" cy="1.5" r="1.5" fill="#2b2b2b"/></svg>
    </div>
  </header>

  <section class="hero" role="img" aria-label="Close-up of a gold pendant on dark plum fabric">
    <div class="hero-text">
      <h1>ELEGANCE BY NATURE</h1>
      <p>Elegance, sophistication and a thirst for innovation</p>
      <span class="btn-outline">SHOP NOW</span>
    </div>
    <div class="hero-controls">
      <svg width="8" height="9" viewBox="0 0 8 9"><path d="M0 0l8 4.5L0 9z" fill="var(--gold)"/></svg>
      <svg width="8" height="9" viewBox="0 0 8 9"><rect width="3" height="9" fill="#fff"/><rect x="5" width="3" height="9" fill="#fff"/></svg>
    </div>
  </section>

  <section class="themes">
    <h2 class="section-title">PENDANT THEMES</h2>
    <div class="theme-grid">
      <div class="theme"><div class="theme-photo" role="img" aria-label="Model wearing the bee pendant" style="background:linear-gradient(160deg,#e8d6c6,#a87c64)"></div><h3>BEE</h3><small>the pendant of abundance</small><span class="btn-mini">VIEW COLLECTION</span></div>
      <div class="theme"><div class="theme-photo" role="img" aria-label="Model wearing the dragon pendant" style="background:linear-gradient(160deg,#2f8c8e,#1e4e55)"></div><h3>DRAGON</h3><small>the pendant of protection</small><span class="btn-mini">VIEW COLLECTION</span></div>
      <div class="theme"><div class="theme-photo" role="img" aria-label="Model wearing the dragonfly pendant" style="background:linear-gradient(160deg,#7ec0bd,#4b6d70)"></div><h3>DRAGONFLY</h3><small>the pendant of enlightenment</small><span class="btn-mini">VIEW COLLECTION</span></div>
      <div class="theme"><div class="theme-photo" role="img" aria-label="Model wearing the frog pendant" style="background:linear-gradient(160deg,#3a2a2c,#160f12)"></div><h3>FROG</h3><small>the pendant of transformation</small><span class="btn-mini">VIEW COLLECTION</span></div>
      <div class="theme"><div class="theme-photo" role="img" aria-label="Model wearing the ladybird pendant" style="background:linear-gradient(160deg,#c44a4a,#4a1c20)"></div><h3>LADYBIRD</h3><small>the pendant of good fortune</small><span class="btn-mini">VIEW COLLECTION</span></div>
      <div class="theme"><div class="theme-photo" role="img" aria-label="Model wearing the toucan pendant" style="background:linear-gradient(160deg,#9a9a9a,#4a4e52)"></div><h3>TOUCAN</h3><small>the pendant of charisma</small><span class="btn-mini">VIEW COLLECTION</span></div>
    </div>
    <div class="divider"></div>
  </section>

  <section class="shop">
    <h2 class="section-title">SHOP NOW</h2>
    <p class="section-lead">Lorem ipsum dolor sit amet conse ctetur adipisicing elit, sed do eiusmod tempor incididunt ut labore</p>
    <div class="product-grid">
      <div><div class="product-card"><div class="necklace" role="img" aria-label="Gold bee pendant on purple bead chain" style="background:radial-gradient(circle at 50% 50%,#f1dfae 0,#fff 45%)"></div><div class="cart-bar"><span>🛒 ADD TO CART</span><span style="margin-left:auto">♥</span><span>◉</span></div></div><div class="product-info"><h4>Bee-Gold-Amethyst</h4><div class="stars">★★★★★</div><div class="price">$ 130.00</div></div></div>
      <div><div class="product-card"><div class="necklace" role="img" aria-label="Gold dragon pendant with amazonite stone" style="background:radial-gradient(circle at 50% 50%,#e9d6a4 0,#fff 45%)"></div></div><div class="product-info"><h4>Dragon-Gold-Amazonite</h4><div class="stars">★★★★★</div><div class="price">$ 130.00</div></div></div>
      <div><div class="product-card"><div class="necklace" role="img" aria-label="Rhodium dragon pendant with citrine stone" style="background:radial-gradient(circle at 50% 50%,#dcdcdc 0,#fff 45%)"></div></div><div class="product-info"><h4>Dragon-Rhodium-Citrine</h4><div class="stars">★★★★★</div><div class="price">$ 130.00<s>$ 150.00</s></div></div></div>
      <div><div class="product-card"><div class="necklace" role="img" aria-label="Gold dragonfly pendant with amethyst stone" style="background:radial-gradient(circle at 50% 50%,#f0dca6 0,#fff 45%)"></div></div><div class="product-info"><h4>Dragonfly-Gold-Amethyst</h4><div class="stars">★★★★★</div><div class="price">$ 130.00<s>$ 150.00</s></div></div></div>
      <div><div class="product-card"><div class="necklace" role="img" aria-label="Rhodium frog pendant with black spinel" style="background:radial-gradient(circle at 50% 50%,#d4d4d4 0,#fff 45%)"></div></div><div class="product-info"><h4>Frog-Rhodium-Black Spinel</h4><div class="stars">★★★★★</div><div class="price">$ 130.00</div></div></div>
      <div><div class="product-card"><div class="necklace" role="img" aria-label="Gold ladybird pendant with citrine" style="background:radial-gradient(circle at 50% 50%,#efd9a0 0,#fff 45%)"></div></div><div class="product-info"><h4>Ladybird-Gold-Citrine</h4><div class="stars">★★★★★</div><div class="price">$ 130.00</div></div></div>
      <div><div class="product-card"><div class="necklace" role="img" aria-label="Rhodium toucan pendant with labradorite" style="background:radial-gradient(circle at 50% 50%,#d6d6d6 0,#fff 45%)"></div></div><div class="product-info"><h4>Toucan-Rhodium-Labradorite</h4><div class="stars">★★★★★</div><div class="price">$ 130.00<s>$ 150.00</s></div></div></div>
      <div><div class="product-card"><div class="necklace" role="img" aria-label="Rhodium frog pendant with amazonite" style="background:radial-gradient(circle at 50% 50%,#cfe7e2 0,#fff 45%)"></div></div><div class="product-info"><h4>Frog-Rhodium-Amazonite</h4><div class="stars">★★★★★</div><div class="price">$ 130.00<s>$ 150.00</s></div></div></div>
    </div>
    <div class="view-more"><span class="btn-mini" style="font-size:6px;padding:4px 10px">VIEW MORE</span></div>
  </section>

  <section class="promo">
    <div class="promo-portrait" role="img" aria-label="Portrait of the jewelry designer"></div>
    <div class="promo-text">
      <h2>MY CREATIONS, A HOMAGE TO MOTHER EARTH</h2>
      <p>Themed Pendants can be mixed and matched with interchangeable<br>fine gemstones thanks to snap rings.</p>
      <span class="btn-outline">SHOP NEW COLLECTIONS</span>
    </div>
  </section>

  <section class="blog">
    <h2 class="section-title">LATEST BLOGS</h2>
    <p class="section-lead">Lorem ipsum dolor amet consectet adipisicing elit, sedo eiusmod tempor incididunt ulabore</p>
    <div class="blog-grid">
      <article>
        <div class="blog-photo" role="img" aria-label="Magazine feature portrait with white roses" style="background:linear-gradient(135deg,#6b5a45,#c9a78a 50%,#e9e2d6)"></div>
        <div class="blog-body"><div class="date"><b>08</b><i>AUG</i></div><div><h5>SED UT PERSPICIATIS UNDE OMNIS ISTE NATUS</h5><p>Sed ut perspiciatis unde omnis iste natus error sit voluptatem accusantium doloremque laudantium, totam rem aperiam, eaque ipsa quae ab illo inventore veritatis et quasi architecto beatae vitae dicta sunt explicabo.</p></div></div>
      </article>
      <article>
        <div class="blog-photo" role="img" aria-label="Magazine cover portrait" style="background:linear-gradient(135deg,#3a2b24,#7a5a48 55%,#d8cfc2)"></div>
        <div class="blog-body"><div class="date"><b>08</b><i>AUG</i></div><div><h5>SED UT PERSPICIATIS UNDE OMNIS ISTE NATUS</h5><p>Sed ut perspiciatis unde omnis iste natus error sit voluptatem accusantium doloremque laudantium, totam rem aperiam, eaque ipsa quae ab illo inventore veritatis et quasi architecto beatae vitae dicta sunt explicabo.</p></div></div>
      </article>
    </div>
  </section>

  <footer class="footer">
    <div class="partners"><span>HALVARD STUDIO</span><span>ORRIN WORKS</span><span>MERROW &amp; CO</span><span>QUILLFIELD</span><span>BRISK LANE</span></div>
    <div class="foot-cols">
      <div><h6>KEEP IN TOUCH</h6><p>⌖ Lorem ipsum street 12<br>Geneva, Switzerland<br>✆ +41 22 000 00 00<br>✉ info@velmorik.com</p></div>
      <div><h6>SOCIAL CONNECT</h6><p>Sed ut perspiciatis unde omnis iste natus error sit voluptatem<br>accusantium doloremque laudantium, totam rem aperiam,<br>eaque ipsa quae ab illo inventore.</p><div class="socials"><span></span><span></span><span></span><span></span></div></div>
      <div><h6>JOIN OUR EMAIL</h6><p>Sed ut perspiciatis unde omnis iste natus error sit voluptatem<br>accusantium doloremque laudantium.</p><div class="subscribe"><span>Your Email...</span><b>SUBSCRIBE</b></div></div>
    </div>
    <div class="foot-links">
      <div class="foot-brand"><div class="brand" style="align-items:flex-start"><div class="brand-mark" style="margin-left:26px"></div><div class="brand-name">TRÉVI MANU</div><div class="brand-sub">JEWELRY</div></div><p>Diam, eaque ipsa quae ab illo inventore veritatis<br>quasi architecto beatae vitae dicta.</p></div>
      <div><h6>Information</h6><ul><li>› Home</li><li>› About Us</li><li>› Products</li><li>› Privacy Policy</li></ul></div>
      <div><h6>Extras</h6><ul><li>› Offers</li><li>› Gift Certificates</li><li>› Affiliate</li><li>› Specials</li></ul></div>
      <div><h6>My Account</h6><ul><li>› Our Company</li><li>› Blog</li><li>› Our Proposal</li><li>› Contact Us</li></ul></div>
      <div><h6>Instagram</h6><div class="insta" role="img" aria-label="Recent jewelry photos"><span></span><span></span><span></span><span></span><span></span><span></span><span></span><span></span></div></div>
    </div>
    <div class="copyright">Copyright © 2019 | All Rights Reserved</div>
  </footer>

</div>
</body>
</html>
```